Refresh of Business Card Design

Want to refresh the business card design with the new logo while adhering to style guide as attached. Would like to match feel of website www.durmackvinex.com

```html
<!DOCTYPE html>
<html lang="en">
<head>
<meta charset="utf-8">
<title>Durmack Vinex – Business Card</title>
<link rel="stylesheet" href="https://fonts.googleapis.com/css2?family=Work+Sans:wght@400;500;600&display=swap">
<style>
  :root {
    --page: #ffffff;
    --card: #000000;
    --text: #ffffff;
    --accent: #e8193c;
    --silver-light: #f2f2f2;
    --silver-mid: #9a9a9a;
    --silver-dark: #4a4a4a;
    --sheen: #1c1c1c;
  }
  * { box-sizing: border-box; margin: 0; padding: 0; }
  html, body {
    width: 1200px; height: 1200px; overflow: hidden;
    background: var(--page);
    font-family: "Work Sans", Arial, sans-serif;
    color: var(--text);
  }
  .card {
    position: absolute;
    left: 250px;
    width: 698px;
    height: 419px;
    background: var(--card);
    overflow: hidden;
  }
  .card--front { top: 117px; }
  .card--back { top: 642px; }

  .wordmark {
    position: absolute;
    display: flex;
    align-items: center;
    gap: 14px;
    font-weight: 600;
    letter-spacing: 0.04em;
    white-space: nowrap;
  }
  .wordmark__dot {
    border-radius: 50%;
    background: var(--accent);
    flex: none;
  }
  .card--front .wordmark {
    left: 50%; top: 157px;
    transform: translate(-50%, -50%);
    font-size: 36px;
  }
  .card--front .wordmark__dot { width: 44px; height: 44px; }

  .front__rule {
    position: absolute;
    left: 0; right: 0; top: 313px;
    height: 4px;
    background: linear-gradient(90deg, var(--silver-dark), var(--silver-light) 30%, var(--silver-mid) 60%, var(--silver-light) 85%, var(--silver-dark));
  }
  .front__url {
    position: absolute;
    left: 0; right: 0; top: 355px;
    text-align: center;
    font-size: 19px;
    letter-spacing: 0.62em;
    padding-left: 0.62em;
  }

  .back__sheen {
    position: absolute;
    top: 0; right: 0; bottom: 0;
    width: 330px;
    background: linear-gradient(135deg, var(--card) 0%, var(--sheen) 55%, var(--card) 100%);
  }
  .card--back .wordmark {
    left: 545px; top: 108px;
    transform: translate(-50%, -50%);
    font-size: 20px;
    gap: 9px;
  }
  .card--back .wordmark__dot { width: 24px; height: 24px; }

  .person { position: absolute; left: 54px; top: 90px; }
  .person__name {
    font-size: 31px; font-weight: 600;
    color: var(--accent);
    letter-spacing: 0.01em;
    line-height: 1;
  }
  .person__role {
    margin-top: 12px; margin-left: 6px;
    font-size: 17px; letter-spacing: 0.04em;
  }

  .contact {
    position: absolute; left: 52px; top: 218px;
    list-style: none;
    font-size: 19px; line-height: 27px;
  }
  .contact__item { display: flex; gap: 10px; margin-bottom: 8px; }
  .contact__icon { width: 18px; height: 18px; margin-top: 4px; flex: none; fill: var(--accent); }
</style>
</head>
<body>
  <section class="card card--front" aria-label="Card front">
    <div class="wordmark"><span class="wordmark__dot"></span>DURMACK VINEX</div>
    <div class="front__rule"></div>
    <p class="front__url">DURMACKVINEX.COM</p>
  </section>

  <section class="card card--back" aria-label="Card back">
    <div class="back__sheen" role="img" aria-label="Decorative silver swoosh ornament area"></div>

    <div class="wordmark"><span class="wordmark__dot"></span>DURMACK VINEX</div>

    <div class="person">
      <h1 class="person__name">REID CALLOWAY</h1>
      <p class="person__role">SALES</p>
    </div>

    <ul class="contact">
      <li class="contact__item">
        <svg class="contact__icon" viewBox="0 0 24 24" aria-hidden="true"><path d="M6.6 10.8a15.1 15.1 0 0 0 6.6 6.6l2.2-2.2a1 1 0 0 1 1-.25 11.4 11.4 0 0 0 3.6.57 1 1 0 0 1 1 1V20a1 1 0 0 1-1 1A17 17 0 0 1 3 4a1 1 0 0 1 1-1h3.5a1 1 0 0 1 1 1c0 1.25.2 2.45.57 3.57a1 1 0 0 1-.25 1z"/></svg>
        <span>806-555-0147</span>
      </li>
      <li class="contact__item">
        <svg class="contact__icon" viewBox="0 0 24 24" aria-hidden="true"><path d="M2 5h20v14H2z M2 5l10 7 10-7" stroke="#000" stroke-width="1.5"/></svg>
        <span>48210 Halden, TX79902<br>275 Ridgeway Dr Lorne,<br>Texas79340</span>
      </li>
      <li class="contact__item">
        <svg class="contact__icon" viewBox="0 0 24 24" aria-hidden="true"><path d="M12 2a10 10 0 1 0 5 18.7l-1-1.7A8 8 0 1 1 20 12v1.2a1.8 1.8 0 0 1-3.6 0V7h-2v1A5 5 0 1 0 15 16a3.8 3.8 0 0 0 7-2.8V12A10 10 0 0 0 12 2zm0 13a3 3 0 1 1 0-6 3 3 0 0 1 0 6z"/></svg>
        <span>Rcalloway@durmackvinex.com</span>
      </li>
    </ul>
  </section>
</body>
</html>
```